Professional Law Firm Rebranding Brochure Layout Design

Our law firm is changing its name from The Law Office of Dana Moreno, PLLC to MORENO.LAW. I would like a 4-page color brochure (cover, page 2, page 3, back) that announces and explains our rebranding. I have attached lots of files that should be helpful. I envision the words "The Law Office of Dana Moreno, PLLC is now known as MORENO.LAW" at the top of the front cover. Feel free to review our website at https://moreno-legal.example to get an idea of the look and feel we like. Tall buildings and other professional images work well.

Target Market(s)

Businesses, law firm clients, entrepreneurs, startups, corporations

Industry/Entity Type

Legal

Font styles to use
Sans Serif

Colors
cfdeed
85abd2
3276b5
0555a3
cee9f5
85cae6
33a6d7
0492cd

Requirements
Must have
• Professional appearance, photos & bios of team members, explanation of rebranding - finished product is US letter size

```html
<!DOCTYPE html>
<html lang="en">
<head>
<meta charset="utf-8">
<title>MORENO.LAW Rebranding Brochure</title>
<link rel="stylesheet" href="https://fonts.googleapis.com/css2?family=Open+Sans:wght@400;600;700&display=swap">
<style>
:root{
  --bg:#e9eaeb;
  --ice:#cfdeed;
  --mist:#85abd2;
  --blue:#3276b5;
  --navy:#0555a3;
  --sky-pale:#cee9f5;
  --sky:#85cae6;
  --cyan:#33a6d7;
  --azure:#0492cd;
  --deep:#063f7c;
  --white:#ffffff;
  --ink:#3a4350;
  --paper:#fbfbfb;
}
*{box-sizing:border-box;margin:0;padding:0}
html,body{width:1200px;height:2436px;overflow:hidden;background:var(--bg);font-family:"Open Sans",Arial,sans-serif;color:var(--ink)}
.stage{position:relative;width:1200px;height:2436px}
.page{position:absolute;width:520px;height:673px;overflow:hidden;box-shadow:0 14px 30px rgba(0,0,0,.18)}
.spread{position:absolute;left:80px;width:1040px;height:673px;box-shadow:0 14px 30px rgba(0,0,0,.18)}
.spread .page{box-shadow:none;top:0}
.spread .page.left{left:0}
.spread .page.right{left:520px}
.spread::after{content:"";position:absolute;left:516px;top:0;width:8px;height:100%;background:linear-gradient(90deg,rgba(0,0,0,0),rgba(0,0,0,.12),rgba(0,0,0,0));pointer-events:none}
.layer{position:absolute;inset:0}

/* cover */
.cover{background:linear-gradient(160deg,var(--azure) 0%,var(--blue) 55%,var(--navy) 100%)}
.firm-name{position:absolute;left:60px;top:66px;font-weight:600;font-size:36px;color:var(--white);line-height:1.1}
.announce{position:absolute;left:60px;top:120px;width:400px;font-size:13px;line-height:1.5;color:var(--white)}

/* back page */
.back{background:var(--paper)}
.back-copy{position:absolute;left:40px;top:445px;width:440px;font-size:9.5px;line-height:1.5;color:var(--white)}
.connect{position:absolute;left:40px;top:520px;font-size:15px;font-weight:600;color:var(--white)}
.office{position:absolute;top:555px;font-size:9.5px;line-height:1.5;color:var(--white);padding-left:16px}
.office strong{font-weight:600}
.office svg{position:absolute;left:0;top:1px}
.office.one{left:40px}
.office.two{left:290px}
.mark-dot{position:absolute;width:44px;height:44px;background:var(--azure);border-radius:50%}

/* inside left */
.inside-left{background:var(--paper)}
.body-copy{position:absolute;left:46px;top:330px;width:428px;font-size:9px;line-height:1.55;color:var(--ink)}
.body-copy p{margin-bottom:9px}

/* inside right: team */
.team{background:var(--paper)}
.team-title{position:absolute;left:0;right:0;top:48px;text-align:center;font-size:17px;font-weight:600;color:var(--white);letter-spacing:1px}
.grid{position:absolute;left:34px;top:100px;width:452px;display:grid;grid-template-columns:repeat(3,140px);column-gap:16px;row-gap:30px}
.member-photo{height:118px;background:linear-gradient(180deg,var(--ice),var(--mist))}
.member-name{background:var(--azure);color:var(--white);text-align:center;padding:5px 4px;font-size:10px;font-weight:600;line-height:1.25}
.member-name span{display:block;font-size:8px;font-weight:400;opacity:.9}
.member-bio{font-size:7.5px;line-height:1.45;margin-top:7px;color:var(--ink)}
.foot-band{position:absolute;left:0;right:0;bottom:0;height:14px;background:var(--azure)}
</style>
</head>
<body>
<main class="stage">

  <section class="page cover" style="left:340px;top:50px">
    <svg class="layer" width="520" height="673" viewBox="0 0 520 673">
      <defs>
        <linearGradient id="towerA" x1="0" y1="0" x2="0" y2="1">
          <stop offset="0" stop-color="#8fb9dc"/>
          <stop offset=".5" stop-color="#4f7fa6"/>
          <stop offset="1" stop-color="#1f3d5c"/>
        </linearGradient>
      </defs>
      <polygon points="0,190 520,300 520,400 0,300" fill="#063f7c" opacity=".35"/>
      <polygon role="img" aria-label="Photo of a glass office tower against a blue sky" points="150,673 520,250 520,673" fill="url(#towerA)"/>
      <polygon points="0,520 260,673 0,673" fill="#063f7c" opacity=".3"/>
    </svg>
    <div class="firm-name">MORENO.LAW</div>
    <p class="announce">The Law Office of Dana Moreno, PLLC is now known as MORENO.LAW</p>
  </section>

  <section class="spread" style="top:870px">
    <div class="page left back">
      <svg class="layer" width="520" height="673" viewBox="0 0 520 673">
        <defs>
          <linearGradient id="court" x1="0" y1="0" x2="1" y2="1">
            <stop offset="0" stop-color="#c9ced4"/>
            <stop offset="1" stop-color="#6d7782"/>
          </linearGradient>
          <linearGradient id="backBlue" x1="0" y1="0" x2="1" y2="1">
            <stop offset="0" stop-color="#0492cd"/>
            <stop offset="1" stop-color="#0555a3"/>
          </linearGradient>
        </defs>
        <polygon role="img" aria-label="Photo of a courtroom with scales of justice" points="110,0 520,0 520,330 110,200" fill="url(#court)"/>
        <polygon points="0,0 110,0 110,200 0,260" fill="#f2f3f4"/>
        <polygon points="110,200 520,330 520,380 0,390 0,260" fill="#3276b5" opacity=".85"/>
        <polygon points="0,390 520,380 520,673 0,673" fill="url(#backBlue)"/>
      </svg>
      <div class="mark-dot" style="left:48px;top:190px"></div>
      <p class="back-copy">MORENO.LAW helps growing companies and their owners handle legal matters with clear advice and steady support. Reach out today to learn how our team can help your business move forward with confidence.</p>
      <div class="connect">Connect with Dana Moreno</div>
      <div class="office one">
        <svg width="10" height="13" viewBox="0 0 10 13"><path d="M5 0a5 5 0 0 1 5 5c0 3.5-5 8-5 8S0 8.5 0 5a5 5 0 0 1 5-5z" fill="#fff"/><circle cx="5" cy="5" r="1.8" fill="#0555a3"/></svg>
        <strong>Uptown Office</strong><br>120 Harbor Street, Suite 400<br>Riverton, NC 28000
      </div>
      <div class="office two">
        <svg width="10" height="13" viewBox="0 0 10 13"><path d="M5 0a5 5 0 0 1 5 5c0 3.5-5 8-5 8S0 8.5 0 5a5 5 0 0 1 5-5z" fill="#fff"/><circle cx="5" cy="5" r="1.8" fill="#0555a3"/></svg>
        <strong>Lakeside Office</strong><br>48 Mill Lane<br>Lakeside, NC 28001
      </div>
    </div>

    <div class="page right cover">
      <svg class="layer" width="520" height="673" viewBox="0 0 520 673">
        <defs>
          <linearGradient id="towerB" x1="0" y1="0" x2="0" y2="1">
            <stop offset="0" stop-color="#8fb9dc"/>
            <stop offset=".5" stop-color="#4f7fa6"/>
            <stop offset="1" stop-color="#1f3d5c"/>
          </linearGradient>
        </defs>
        <polygon points="0,190 520,300 520,400 0,300" fill="#063f7c" opacity=".35"/>
        <polygon role="img" aria-label="Photo of a glass office tower against a blue sky" points="150,673 520,250 520,673" fill="url(#towerB)"/>
        <polygon points="0,520 260,673 0,673" fill="#063f7c" opacity=".3"/>
      </svg>
      <div class="firm-name">MORENO.LAW</div>
      <p class="announce">The Law Office of Dana Moreno, PLLC is now known as MORENO.LAW</p>
    </div>
  </section>

  <section class="spread" style="top:1690px">
    <div class="page left inside-left">
      <svg class="layer" width="520" height="673" viewBox="0 0 520 673">
        <defs>
          <linearGradient id="meeting" x1="0" y1="0" x2="1" y2="1">
            <stop offset="0" stop-color="#dfe4ea"/>
            <stop offset="1" stop-color="#8a98a8"/>
          </linearGradient>
        </defs>
        <polygon role="img" aria-label="Photo of a business handshake over a desk with documents" points="0,0 520,0 520,150 0,250" fill="url(#meeting)"/>
        <polygon points="0,210 230,170 0,300" fill="#0555a3"/>
        <polygon points="230,170 520,150 520,175 0,300" fill="#3276b5" opacity=".7"/>
        <rect x="0" y="659" width="520" height="14" fill="#0492cd"/>
      </svg>
      <div class="mark-dot" style="left:400px;top:180px"></div>
      <div class="body-copy">
        <p>At MORENO.LAW, we strive to help our clients avoid costly legal mistakes. Preventing legal problems is always cheaper and easier than fixing them after they occur, which is why our attorneys and staff pride themselves on anticipating client needs and meeting them.</p>
        <p>Our primary areas of practice are business law and intellectual property. Our clients range from entrepreneurs and startup companies to established corporations. We understand that owners of every size of company need quick answers and sound advice on business decisions.</p>
        <p>Our goal is to assist our clients by providing high quality work product and creative legal solutions to their legal problems. Our new name reflects this focus on growing businesses and the value we bring to each client relationship.</p>
        <p>We would welcome the opportunity to earn a place as your trusted business advisor. To learn more about MORENO.LAW, please contact us at info@moreno-legal.example or 555-010-0188.</p>
      </div>
    </div>

    <div class="page right team">
      <svg class="layer" width="520" height="673" viewBox="0 0 520 673">
        <defs>
          <linearGradient id="office" x1="0" y1="0" x2="0" y2="1">
            <stop offset="0" stop-color="#3276b5"/>
            <stop offset=".6" stop-color="#85cae6"/>
            <stop offset="1" stop-color="#fbfbfb"/>
          </linearGradient>
        </defs>
        <rect role="img" aria-label="Photo of a bright office hallway with people walking" x="0" y="0" width="520" height="200" fill="url(#office)"/>
      </svg>
      <h2 class="team-title">OUR TEAM MEMBERS</h2>
      <div class="grid">
        <article class="member">
          <div class="member-photo" role="img" aria-label="Portrait photo of team member"></div>
          <div class="member-name">Sofia Lane<span>Office Manager</span></div>
          <p class="member-bio">Sofia keeps the firm running smoothly and is the first point of contact for new and existing clients.</p>
        </article>
        <article class="member">
          <div class="member-photo" role="img" aria-label="Portrait photo of team member"></div>
          <div class="member-name">Evan Dawson<span>Attorney</span></div>
          <p class="member-bio">Evan advises startups on contracts, formation and trademarks, helping founders protect their ideas early.</p>
        </article>
        <article class="member">
          <div class="member-photo" role="img" aria-label="Portrait photo of team member"></div>
          <div class="member-name">Dana Moreno<span>Managing Attorney</span></div>
          <p class="member-bio">Dana founded the firm to give growing businesses practical, timely legal guidance at every stage.</p>
        </article>
        <article class="member">
          <div class="member-photo" role="img" aria-label="Portrait photo of team member"></div>
          <div class="member-name">Carla Reyes<span>Paralegal</span></div>
          <p class="member-bio">Carla supports our attorneys with filings and research, keeping every client matter on schedule.</p>
        </article>
        <article class="member">
          <div class="member-photo" role="img" aria-label="Portrait photo of team member"></div>
          <div class="member-name">Amy Ruiz<span>Paralegal</span></div>
          <p class="member-bio">Amy manages trademark work and client records with care, attention to detail and a friendly voice.</p>
        </article>
        <article class="member">
          <div class="member-photo" role="img" aria-label="Portrait photo of team member"></div>
          <div class="member-name">Lena Park<span>Attorney</span></div>
          <p class="member-bio">Lena focuses on business transactions and helps owners plan deals, partnerships and growth.</p>
        </article>
      </div>
      <div class="foot-band"></div>
    </div>
  </section>

</main>
</body>
</html>
```